Help me create an amazing cover for my first ebook!!

I am looking to have a modern and professional looking cover for my first ebook. It will be published through Borvex Quill Self Press and will need to follow their formatting and guidelines. I want the cover to have a modern and vibrant feel, that appeals to a millennial audience. This is a real estate book that is focused on a niche category catered to young professionals, so the idea would be to appeal to them.

Title:
The Twentysomething Playbook for Duplex Living

A Smart Property Buying Plan to Start Early, Cut Your Housing Costs (Sometimes to Zero), and Speed Up Your Path to Lasting Wealth.

Davin Osterlund

Target Market(s)

Real Estate investors, investors, millennials, young professionals, college educated, 20-40 years old.Financial freedom, finance.

Industry/Entity Type

Real Estate

Font styles to use
Sans Serif

Colors

Designer to choose colors to be used in the design.

Requirements
Must have
• Must follow the borvex quill self press format. I attached a screenshot of the details, it can also be found here: https://qsp.borvexbooks.example/en_US/help/topic/R481736025
• Must include this title:
• The Twentysomething Playbook for Duplex Living
• A Smart Property Buying Plan to Start Early, Cut Your Housing Costs (Sometimes to Zero), and Speed Up Your Path to Lasting Wealth.
• Davin Osterlund.
• I added examples of book covers I like to use as a guide, I also added some color pallette examples.
Nice to have
• Modern, clean design that's not too busy. Some sort of simple photo or illustration to incorporate in the cover along with the text would be nice.

```html
<!DOCTYPE html>
<html lang="en">
<head>
<meta charset="utf-8">
<title>The Twentysomething Playbook for Duplex Living — Davin Osterlund</title>
<link rel="stylesheet" href="https://fonts.googleapis.com/css2?family=Montserrat:wght@500;600;700;800&display=swap">
<style>
  :root {
    --paper: #ffffff;
    --lime: #c8d644;
    --slate: #43545b;
    --teal: #86d1d8;
    --orange: #e8751a;
    --ink: #3f4e55;
    --mist: #dbe7ea;
    --white: #ffffff;
  }
  html, body {
    margin: 0;
    padding: 0;
    overflow: hidden;
    background: var(--paper);
  }
  .cover {
    position: relative;
    width: 750px;
    height: 1200px;
    overflow: hidden;
    background: var(--paper);
    font-family: "Montserrat", Arial, sans-serif;
  }
  .cover-shapes {
    position: absolute;
    inset: 0;
    width: 750px;
    height: 1200px;
  }
  .author {
    position: absolute;
    top: 60px;
    left: 0;
    width: 750px;
    margin: 0;
    text-align: center;
    font-weight: 500;
    font-size: 26px;
    letter-spacing: 0.2em;
    color: var(--ink);
    line-height: 1;
  }
  .title {
    margin: 0;
    font-weight: 800;
  }
  .title-line {
    position: absolute;
    left: 0;
    width: 750px;
    text-align: center;
    line-height: 1;
    display: block;
  }
  .title-lead {
    top: 616px;
    font-size: 45px;
    font-weight: 800;
    color: var(--teal);
  }
  .title-main {
    top: 686px;
    font-size: 104px;
    font-weight: 800;
    letter-spacing: -2px;
    color: var(--lime);
  }
  .title-joiner {
    top: 818px;
    left: 77px;
    width: 596px;
    display: flex;
    align-items: center;
    gap: 14px;
    font-size: 30px;
    font-weight: 700;
    color: var(--white);
  }
  .title-joiner::before,
  .title-joiner::after {
    content: "";
    flex: 1;
    height: 3px;
    background: var(--orange);
  }
  .title-close {
    top: 856px;
    font-size: 64px;
    font-weight: 700;
    color: var(--white);
  }
  .rule-bottom {
    position: absolute;
    top: 930px;
    left: 77px;
    width: 596px;
    height: 3px;
    background: var(--orange);
  }
  .subtitle {
    position: absolute;
    top: 958px;
    left: 50px;
    width: 650px;
    margin: 0;
    text-align: center;
    font-weight: 500;
    font-size: 27px;
    line-height: 37px;
    letter-spacing: 0.02em;
    text-transform: uppercase;
    color: var(--mist);
  }
</style>
</head>
<body>
  <main class="cover">
    <svg class="cover-shapes" viewBox="0 0 750 1200" aria-hidden="true">
      <defs>
        <linearGradient id="portrait-tone" x1="0" y1="0" x2="0" y2="1">
          <stop offset="0" stop-color="#d8bfae"/>
          <stop offset="0.4" stop-color="#6d5a52"/>
          <stop offset="1" stop-color="#2e2e31"/>
        </linearGradient>
      </defs>
      <polygon class="band-lime" points="0,0 750,0 750,44 164,206 0,32" fill="var(--lime)"/>
      <polygon class="band-slate" points="0,344 204,582 750,428 750,1200 0,1200" fill="var(--slate)"/>
    </svg>
    <svg class="cover-shapes" viewBox="0 0 750 1200">
      <rect class="portrait" x="96" y="104" width="578" height="474" rx="28"
            fill="url(#portrait-tone)" role="img"
            aria-label="Photo of a smiling young businesswoman in a dark suit, pointing left and holding up a small orange paper house"/>
    </svg>

    <p class="author">DAVIN OSTERLUND</p>

    <h1 class="title">
      <span class="title-line title-lead">THE TWENTYSOMETHING</span>
      <span class="title-line title-main">PLAYBOOK</span>
      <span class="title-line title-joiner">for</span>
      <span class="title-line title-close">DUPLEX LIVING</span>
    </h1>
    <div class="rule-bottom"></div>

    <p class="subtitle">A smart property buying plan<br>to start early, cut your housing<br>costs (sometimes to zero), and<br>speed up your path<br>to lasting wealth.</p>
  </main>
</body>
</html>
```